Brisk Meadow Builders needs an updated flyer

Instructions are in a .pdf called "Instructions. All photos and logos are included along with the original flyer in .ai

We are looking for a fresh design that promotes sustainability.

```html
<!DOCTYPE html>
<html lang="en">
<head>
<meta charset="utf-8">
<title>Brisk Meadow Builders – Hay Barn House Mini</title>
<link rel="stylesheet" href="https://fonts.googleapis.com/css2?family=Heebo:wght@700;800;900&family=Montserrat:wght@400;500;600&display=swap">
<style>
:root{
  --backdrop:#231f20;
  --orange:#e09f33;
  --green:#5ea553;
  --ink:#1a1a1a;
  --text:#2b2b2b;
  --white:#ffffff;
  --strike:#d0282b;
  --photo-a:#6c8a5a;
  --photo-b:#d8dcd8;
  --photo-c:#4a4d50;
}
*{margin:0;padding:0;box-sizing:border-box}
html,body{width:987px;height:1200px;overflow:hidden;background:var(--backdrop)}
body{position:relative;font-family:"Montserrat",sans-serif}
.flyer{position:absolute;left:95px;top:84px;width:796px;height:1030px;background:var(--white);overflow:hidden}
.abs{position:absolute}
.shapes{position:absolute;left:0;top:0;width:796px;height:1030px}
.heading{font-family:"Heebo",sans-serif}

.brand-top{left:556px;top:44px;width:200px;text-align:center;color:var(--white);font-family:"Heebo",sans-serif;font-weight:800;font-size:22px;line-height:1.05;letter-spacing:.5px}
.brand-top .mark{display:block;width:46px;height:46px;border-radius:50%;background:var(--white);margin:0 auto 10px}

.title-the,.title-main,.title-sub,.tagline{right:36px;text-align:right;color:var(--ink);font-family:"Heebo",sans-serif;line-height:1}
.title-the{top:174px;right:270px;font-size:35px;font-weight:800}
.title-main{top:206px;font-size:64px;font-weight:900;letter-spacing:-1px}
.title-sub{top:259px;font-size:40px;font-weight:800}
.tagline{top:300px;right:33px;font-size:21px;font-weight:700}

.price-was{left:320px;top:343px;width:215px;text-align:center;font-family:"Heebo",sans-serif;font-weight:700;font-size:20px;line-height:1.25;color:var(--ink)}
.price-was .old{position:relative;display:inline-block}
.price-was .old::after{content:"";position:absolute;left:-14px;right:-26px;top:52%;height:1.5px;background:var(--strike)}
.price-now{left:566px;top:338px;font-family:"Heebo",sans-serif;color:var(--ink);line-height:1.1}
.price-now .big{font-size:31px;font-weight:900;display:block}
.price-now .monthly{font-size:20px;font-weight:700;display:block;margin-top:1px}

.features{left:46px;top:432px;width:400px;color:var(--text)}
.features h2{font-family:"Heebo",sans-serif;font-weight:800;font-size:27px;color:#333;margin-bottom:5px}
.bullets{list-style:none}
.bullets li{position:relative;padding-left:18px;font-size:13.3px;line-height:16.8px}
.bullets li::before{content:"";position:absolute;left:2px;top:6px;width:5px;height:5px;border-radius:50%;background:var(--ink)}

.options{left:436px;top:428px;width:360px;height:250px;background:var(--orange);padding:18px 20px 0 34px;color:var(--white)}
.options h2{font-family:"Heebo",sans-serif;font-weight:800;font-size:27px;margin-bottom:3px}
.options .bullets li{font-family:"Heebo",sans-serif;font-weight:700;font-size:14px;line-height:16.8px}
.options .bullets li::before{background:var(--white)}
.options .more{font-family:"Heebo",sans-serif;font-weight:800;font-size:26px;line-height:1;margin-top:10px}

.gallery-band{left:0;top:740px;width:796px;height:82px;background:var(--orange)}
.gallery-frame{top:697px;width:218px;height:167px;background:var(--green);padding:6px}
.gallery-frame svg{display:block;width:100%;height:100%}

.use-cases{left:49px;top:876px;font-size:12px;line-height:15.6px;color:var(--ink)}
.use-cases .label{font-weight:600}
.use-cases .label-green{color:var(--green);font-weight:600}
.use-cases .soft{color:var(--green)}

.brand-bottom{left:600px;top:872px;width:150px;text-align:center;color:var(--orange);font-family:"Heebo",sans-serif;font-weight:800;font-size:18px;line-height:1.05}
.brand-bottom .mark{display:block;width:34px;height:34px;background:var(--orange);margin:0 auto 6px}

.cta-ask{right:582px;top:969px;text-align:right;color:var(--white);font-family:"Heebo",sans-serif;font-weight:800;font-size:12px;line-height:15px}
.cta-talk{left:219px;top:960px;color:var(--white);font-family:"Heebo",sans-serif;font-weight:900;font-size:34px;line-height:1}
.contact{left:508px;top:970px;color:var(--white);font-family:"Heebo",sans-serif;font-weight:800}
.contact .row{display:flex;align-items:center;gap:6px}
.contact .web{font-size:13px}
.contact .phone{font-size:32px;line-height:1;margin-top:2px}
.contact svg{flex:none}
</style>
</head>
<body>
<div class="flyer">
  <svg class="shapes" viewBox="0 0 1210 1565" preserveAspectRatio="none" aria-hidden="true">
    <rect x="0" y="0" width="1210" height="570" fill="var(--orange)"/>
    <polygon points="740,0 875,0 540,338 500,300" fill="var(--green)"/>
    <polygon points="520,0 538,0 684,142 268,570 250,570 666,142" fill="var(--white)"/>
    <polygon points="445,482 454,482 370,570 360,570" fill="var(--white)"/>
    <polygon points="455,502 1210,502 1210,618 355,618" fill="var(--green)"/>
    <polygon points="0,1447 635,1447 595,1565 0,1565" fill="var(--green)"/>
    <polygon points="645,1467 1210,1467 1210,1565 612,1565" fill="var(--orange)"/>
  </svg>

  <svg class="abs" style="left:0;top:0" width="796" height="375" viewBox="0 0 1210 570" role="img" aria-label="Photo of a white board-and-batten tiny vending house on a tandem trailer with solar panels and a wooden porch deck">
    <defs>
      <linearGradient id="heroTone" x1="0" y1="0" x2="0" y2="1">
        <stop offset="0" stop-color="var(--photo-a)"/>
        <stop offset=".55" stop-color="var(--photo-b)"/>
        <stop offset="1" stop-color="var(--photo-c)"/>
      </linearGradient>
    </defs>
    <polygon points="0,0 510,0 656,142 250,570 0,570" fill="url(#heroTone)"/>
    <polygon points="0,0 120,0 0,120" fill="#5a5a5a"/>
    <line x1="118" y1="2" x2="2" y2="118" stroke="var(--white)" stroke-width="6"/>
  </svg>

  <div class="abs brand-top"><span class="mark"></span>BRISK MEADOW<br>BUILDERS</div>

  <div class="abs title-the">The</div>
  <div class="abs title-main">“HAY BARN</div>
  <div class="abs title-sub">House Mini”</div>
  <div class="abs tagline">Luxury, mobile vending house</div>

  <div class="abs price-was">Base price starting at<br><span class="old">just $65,000</span></div>
  <div class="abs price-now"><span class="big">Now $45,000</span><span class="monthly">Or just $425/Mo.</span></div>

  <section class="abs features">
    <h2>Base unit features:</h2>
    <ul class="bullets">
      <li>Trailer features tandem wheels w/ brakes</li>
      <li>Steel frame construction for fire retardation safety and weight reduction.</li>
      <li>100% Off grid with solar &amp; up to 20 KWH’s of lithium battery storage allowing trailer to be used in places not accessible by traditional trailers.</li>
      <li>60 Gallon water supply tank</li>
      <li>70 Gallon waste water tank</li>
      <li>Custom interiors to suit various uses</li>
      <li>Multiple sizes from 12’, 16’, 20’ &amp; 24’ long</li>
      <li>Cupboards, cabinets &amp; four stainless steel sinks.</li>
      <li>60" Gas shock serving window</li>
    </ul>
  </section>

  <section class="abs options">
    <h2>Available options:</h2>
    <ul class="bullets">
      <li>HVAC - Norvane Mini Split</li>
      <li>Cooler / Glass front Commercial</li>
      <li>refrigerator</li>
      <li>Upper loft storage area</li>
      <li>Signage and graphics</li>
      <li>Ice machine</li>
      <li>3 foot fold down porch deck</li>
    </ul>
    <p class="more">Other custom options<br>available upon request</p>
  </section>

  <div class="abs gallery-band"></div>
  <div class="abs gallery-frame" style="left:39px">
    <svg viewBox="0 0 206 155" preserveAspectRatio="none" role="img" aria-label="Photo of the tiny house from the side with its serving window open"><defs><linearGradient id="g1" x1="0" y1="0" x2="0" y2="1"><stop offset="0" stop-color="#9bb7d4"/><stop offset=".5" stop-color="#dfe2e0"/><stop offset="1" stop-color="#4d5052"/></linearGradient></defs><rect width="206" height="155" fill="url(#g1)"/></svg>
  </div>
  <div class="abs gallery-frame" style="left:278px">
    <svg viewBox="0 0 206 155" preserveAspectRatio="none" role="img" aria-label="Photo of the tiny house front porch with door and gabled roof"><defs><linearGradient id="g2" x1="0" y1="0" x2="0" y2="1"><stop offset="0" stop-color="#6f9a5c"/><stop offset=".5" stop-color="#e2e4e2"/><stop offset="1" stop-color="#55585a"/></linearGradient></defs><rect width="206" height="155" fill="url(#g2)"/></svg>
  </div>
  <div class="abs gallery-frame" style="left:518px">
    <svg viewBox="0 0 206 155" preserveAspectRatio="none" role="img" aria-label="Photo of the tiny house with solar roof parked in front of trees"><defs><linearGradient id="g3" x1="0" y1="0" x2="0" y2="1"><stop offset="0" stop-color="#4f7a40"/><stop offset=".55" stop-color="#e4e6e4"/><stop offset="1" stop-color="#5a5d60"/></linearGradient></defs><rect width="206" height="155" fill="url(#g3)"/></svg>
  </div>

  <div class="abs use-cases">
    <div class="label-green">Use cases:</div>
    <div><span class="label-green">Food:</span> Lemonade, coffee, pizza, cookies, doughnuts, farm to table etc.</div>
    <div><span class="label">Retail:</span> Grocery / convenience, clothing, watches, jewelry, flowers, crafts, art.</div>
    <div><span class="label">Fundraisers:</span> <span class="soft">Boy/Girl sports, non profits</span></div>
  </div>

  <div class="abs brand-bottom"><span class="mark"></span>BRISK MEADOW<br>BUILDERS</div>

  <div class="abs cta-ask">Need a custom branded<br>solution for your business?</div>
  <div class="abs cta-talk">Let’s talk!”</div>

  <div class="abs contact">
    <div class="row web">
      <svg width="17" height="17" viewBox="0 0 20 20" aria-hidden="true"><circle cx="10" cy="10" r="8.5" fill="none" stroke="var(--white)" stroke-width="1.5"/><path d="M7 6l7 4-3 1-1 3z" fill="var(--white)"/></svg>
      www.BriskMeadowBuilders.com
    </div>
    <div class="row phone">
      <svg width="19" height="19" viewBox="0 0 20 20" aria-hidden="true"><circle cx="10" cy="10" r="8.5" fill="none" stroke="var(--white)" stroke-width="1.5"/><path d="M7 5.5l1.6 2.4-1 1.1a7 7 0 0 0 3.4 3.4l1.1-1 2.4 1.6-.9 1.6c-3.8-.3-7.2-3.7-7.5-7.5z" fill="var(--white)"/></svg>
      555-014-2277
    </div>
  </div>
</div>
</body>
</html>
```